依頼詳細
・余白のある、落ち着いたデザインを希望です。
・以下参考サイトのような色味(キーカラー)を希望です。
(デザインは極端に類似しないことが望ましい)
- https://rinpa-kissa.jp/
- https://hamonoya.com/
・サイトのメニューは
-ごあいさつ
-会社案内・沿革
-事業内容
-納入実績
-お問い合わせ
-みなせのものづくり(ブログ)
-ネットショップ
となる予定です。
この度は、「TOPページのデザイン」と、上記「下層ページのベースデザイン」を依頼いたします。
・レスポンシブでスマートフォンにも対応させます。
・TOPページにはNEWS(お知らせ)欄が入る予定です。
・最終的に当方でWordPressにて構築します。
・参考サイトのイメージにとらわれない自由なデザインでもOKです。
ぜひ様々なアイデアをご提案下さい。
サイトURL
ページ数
2ページ
希望イメージ
シンプル 複雑
単色 カラフル
暗い 明るい
日常 高級
遊び心 厳粛
未来的 伝統的
女性的 男性的
希望する色
茶系、背景は白でお願いいたします。
納品ファイル
• 高解像度JPG (.jpg)
• イラストレーター形式 (.ai)
• フォトショップ形式 (.psd)
• PNG形式 (.png)
補足説明
資料と素材写真を添付いたします。
写真は今後差し替え予定なのでダミーとしてお使いください。

素材画像で購入が必要なものがある場合、「Pexel Vault (https://vault.pexelmart.com/jp/)」より選定下さい。当方で購入しますので、ご提案の際はカンプ画像を利用いただき、採用後には素材のURL or ファイル番号をお伝えいただきます。

その他ご不明な点がございましたら、お気軽にご連絡下さい。

シンプルで飽きの来ないデザインをクライアント様が気に入りました。

この度は本当にたくさんのご提案をいただきましてまことにありがとうございました。
どのデザインも素敵で、選ぶのに時間がかかりまして申し訳ございませんでした。
またの機会がございましたらご提案ください。改めて御礼申し上げます。

```html
<!DOCTYPE html>
<html lang="ja">
<head>
<meta charset="utf-8">
<title>水無瀬みなせ</title>
<link href="https://fonts.googleapis.com/css2?family=Noto+Serif+JP:wght@400;500;600&display=swap" rel="stylesheet">
<style>
:root{
  --brown:#8b6b3e;
  --brown-dark:#5a4026;
  --gold:#b08d57;
  --text:#4a3b2c;
  --muted:#8c7f70;
  --beige:#f5f0e7;
  --line:#d9cdb8;
  --white:#ffffff;
}
*{margin:0;padding:0;box-sizing:border-box}
html,body{width:1200px;height:3792px;overflow:hidden}
body{font-family:"Noto Serif JP",serif;color:var(--text);background:var(--white);position:relative}
.abs{position:absolute}
.site-header{position:absolute;left:0;top:0;width:1200px;height:96px;display:flex;align-items:center;padding:0 0 0 28px;z-index:2}
.brand{display:flex;align-items:center;gap:12px;color:var(--brown-dark);font-size:26px;font-weight:600;letter-spacing:.08em}
.brand-dot{width:34px;height:34px;border-radius:50%;background:var(--brown)}
.global-nav{display:flex;gap:34px;margin-left:auto;margin-right:36px;font-size:15px;color:var(--brown-dark)}
.header-contact{width:180px;height:66px;background:var(--gold);color:var(--white);display:flex;align-items:center;justify-content:center;font-size:16px;letter-spacing:.1em;align-self:flex-start}
.hero{left:0;top:0;width:1200px;height:600px;background:linear-gradient(120deg,#d9b58a 0%,#a9794c 40%,#6e4a2d 75%,#3d2818 100%)}
.news{left:0;top:600px;width:1200px;height:220px;background:var(--beige)}
.news-title{left:268px;top:640px;writing-mode:vertical-rl;font-size:24px;letter-spacing:.3em;color:var(--brown);border-right:2px solid var(--gold);padding-right:8px}
.news-list{left:360px;top:660px;width:560px;list-style:none;font-size:14px}
.news-list li{display:flex;gap:40px;padding:14px 0;border-bottom:1px solid var(--line)}
.news-list time{color:var(--muted)}
.news-more{left:820px;top:780px;font-size:13px;color:var(--muted)}
.intro{left:0;top:930px;width:1200px;text-align:center}
.intro h2{font-size:30px;font-weight:500;line-height:1.7;color:var(--brown-dark);letter-spacing:.12em}
.intro p{width:760px;margin:50px auto 0;text-align:left;font-size:14px;line-height:2.2;color:var(--text)}
.band{left:0;top:1340px;width:1200px;height:320px;background:linear-gradient(90deg,#3f4b63 0%,#7b8192 40%,#c7b79b 70%,#8a7e6f 100%);display:flex;align-items:center;justify-content:center}
.band-label{color:var(--white);font-size:30px;letter-spacing:.15em;font-weight:500}
.section-title{left:0;width:1200px;text-align:center;font-size:32px;color:var(--brown-dark);letter-spacing:.2em;font-weight:500}
.section-title::after{content:"";display:block;width:40px;height:2px;background:var(--gold);margin:16px auto 0}
.services{left:272px;top:1900px;width:656px;display:flex;flex-wrap:wrap;justify-content:center;gap:12px}
.service{width:210px;height:200px;display:flex;align-items:center;justify-content:center}
.service span{background:rgba(255,255,255,.92);padding:8px 14px;font-size:16px;color:var(--brown-dark);letter-spacing:.08em}
.works{left:0;top:2400px;width:1200px;height:540px;display:grid;grid-template-columns:repeat(5,1fr);grid-template-rows:1fr 1fr}
.works div{width:100%;height:100%}
.works-label{left:460px;top:2610px;width:280px;height:120px;background:rgba(255,255,255,.94);display:flex;align-items:center;justify-content:center;font-size:30px;color:var(--brown-dark);letter-spacing:.2em}
.blog-list{left:272px;top:3060px;width:656px;display:flex;gap:28px}
.blog-card{width:200px}
.blog-thumb{width:200px;height:140px}
.blog-card time{display:block;margin-top:12px;font-size:12px;color:var(--muted)}
.blog-card p{font-size:13px;margin-top:4px;padding-bottom:10px;border-bottom:1px solid var(--line)}
.shop-banner{left:272px;top:3350px;width:656px;height:170px;background:linear-gradient(90deg,#d7dbe2,#b9c1cc 50%,#c8b79c);display:flex;align-items:center;justify-content:center}
.shop-banner span{background:var(--white);padding:22px 48px;font-size:18px;color:var(--brown-dark);letter-spacing:.1em}
.site-footer{left:0;top:3580px;width:1200px;height:212px;background:var(--beige)}
.footer-info{left:300px;top:3624px}
.footer-info .brand{font-size:24px}
.footer-info address{font-style:normal;font-size:12px;line-height:1.8;color:var(--muted);margin-top:10px}
.footer-contact{left:584px;top:3668px;width:336px;height:72px;border:1px solid var(--gold);display:flex;align-items:center;justify-content:center;font-size:20px;color:var(--brown);letter-spacing:.15em;background:var(--white)}
</style>
</head>
<body>
<div class="abs hero" role="img" aria-label="木彫りの木型を彫刻刀で削る職人の手元の写真"></div>
<header class="site-header">
  <div class="brand"><span class="brand-dot"></span>水無瀬みなせ</div>
  <nav class="global-nav"><span>ごあいさつ</span><span>会社案内・沿革</span><span>事業内容</span><span>納入実績</span><span>ブログ</span><span>ネットショップ</span></nav>
  <a class="header-contact">お問い合わせ</a>
</header>

<section class="abs news"></section>
<h2 class="abs news-title">お知らせ</h2>
<ul class="abs news-list">
  <li><time>2019/10/10</time><span>ホームページリニューアルのお知らせ</span></li>
  <li><time>2019/10/10</time><span>臨時休業のお知らせ</span></li>
</ul>
<span class="abs news-more">もっと見る →</span>

<section class="abs intro">
  <h2>あなたの思い描いていることを<br>かたちにします</h2>
  <p>水無瀬みなせは、木型の製作を中心に、木工の技術を生かしたものづくりを続けてまいりました。<br>伝統的な菓子木型から看板、祭りの道具まで、職人の手仕事でひとつひとつ仕上げております。<br>お客様の思い描くかたちを丁寧にうかがい、素材選びから仕上げまで心を込めてお届けします。<br>これからも地域の文化とともに歩み、暮らしに寄り添うものづくりを続けてまいります。<br>小さなご相談からでも、どうぞお気軽にお問い合わせください。</p>
</section>

<section class="abs band" role="img" aria-label="祭り人形と山車の写真"><span class="band-label">会社案内・沿革</span></section>

<h2 class="abs section-title" style="top:1770px">事業内容</h2>
<div class="abs services">
  <div class="service" style="background:linear-gradient(135deg,#c99f72,#8a5d38)" role="img" aria-label="木型加工の写真"><span>木型加工</span></div>
  <div class="service" style="background:linear-gradient(135deg,#e7d3b5,#b98d5e)" role="img" aria-label="お菓子木型の写真"><span>お菓子木型</span></div>
  <div class="service" style="background:linear-gradient(135deg,#b47a4a,#6e4a2d)" role="img" aria-label="アート造形彫刻の写真"><span>アート造形彫刻</span></div>
  <div class="service" style="background:linear-gradient(135deg,#c9a77b,#7d5a3a)" role="img" aria-label="看板デザインの写真"><span>看板デザイン</span></div>
  <div class="service" style="background:linear-gradient(135deg,#7f8fa6,#9c6b4a)" role="img" aria-label="祭り道具修理の写真"><span>祭り道具修理</span></div>
</div>

<div class="abs works" role="img" aria-label="納入した木工品と看板の写真の組み合わせ">
  <div style="background:#c7bfb4"></div><div style="background:#8c6a4a"></div><div style="background:#d6cfc4"></div><div style="background:#6f6a66"></div><div style="background:#c9a878"></div>
  <div style="background:#a68560"></div><div style="background:#e2dcd2"></div><div style="background:#9a8570"></div><div style="background:#5d4c40"></div><div style="background:#b99a6e"></div>
</div>
<div class="abs works-label">納入実績</div>

<h2 class="abs section-title" style="top:2970px">ブログ</h2>
<div class="abs blog-list">
  <article class="blog-card"><div class="blog-thumb" role="img" aria-label="祭りの山車の写真" style="background:linear-gradient(135deg,#8fa3c2,#b24a3a)"></div><time>2019.10.10</time><p>ここにテキストが入ります</p></article>
  <article class="blog-card"><div class="blog-thumb" role="img" aria-label="木製スプーンの写真" style="background:linear-gradient(135deg,#e6d8c2,#b0844f)"></div><time>2019.10.10</time><p>ここにテキストが入ります</p></article>
  <article class="blog-card"><div class="blog-thumb" role="img" aria-label="祭り人形の写真" style="background:linear-gradient(135deg,#9fb4cf,#7a6a5c)"></div><time>2019.10.10</time><p>ここにテキストが入ります</p></article>
</div>

<div class="abs shop-banner" role="img" aria-label="木工製品が並ぶオンラインショップの写真"><span>オンラインショップはこちら</span></div>

<footer class="abs site-footer"></footer>
<div class="abs footer-info">
  <div class="brand"><span class="brand-dot"></span>水無瀬みなせ</div>
  <address>有限会社 水無瀬みなせ<br>〒990-0000 山形県水瀬市本町1-2-3<br>TEL 0000-00-0000</address>
</div>
<a class="abs footer-contact">お問い合わせ</a>
</body>
</html>
```